New Property development signage

large poster for a new development.
3 metres x 2 metres. To include the following.

Verrow Gardens
TO LET
LUXURY FULLY FURNISHED LARGE
2 AND 3 BED APARTMENTS
Tallick Estates
362 4105
www.tallickestates-example.com

Need this to be large simple writing with Tallick estates logo on the bottom

Target Market(s)

High end rental property market

Industry/Entity Type

Real Estate Development

Colors
000000
cbcbcb
0555a3

Requirements
Must have
• Name of the development must be in a different font, classic style
Nice to have
• Light Grey background, blues for colours
Should not have
• anymore than 3 /4 colours

```html
<!DOCTYPE html>
<html lang="en">
<head>
<meta charset="utf-8">
<title>Verrow Gardens – To Let</title>
<link rel="stylesheet" href="https://fonts.googleapis.com/css2?family=Cormorant+Garamond:wght@400;500&family=Montserrat:wght@300;400;600&display=swap">
<style>
  :root {
    --ink: #000000;
    --paper: #ffffff;
    --grey: #cbcbcb;
    --blue-deep: #0555a3;
    --blue-mid: #1a7fe6;
    --blue-bright: #13b6f5;
    --cyan: #2ee6ff;
    --line: rgba(255,255,255,0.55);
  }
  html, body {
    margin: 0;
    padding: 0;
    overflow: hidden;
    background: var(--paper);
  }
  .poster {
    position: relative;
    width: 800px;
    height: 1200px;
    overflow: hidden;
    background: var(--paper);
    font-family: "Montserrat", Arial, sans-serif;
  }
  .hero-panel {
    position: absolute;
    left: 0;
    top: 46px;
    width: 800px;
    height: 912px;
    background:
      radial-gradient(ellipse 60% 45% at 60% 30%, var(--cyan) 0%, rgba(46,230,255,0) 70%),
      linear-gradient(180deg, var(--blue-bright) 0%, var(--blue-mid) 60%, #1366dd 100%);
  }
  .hero-panel svg.swoosh {
    position: absolute;
    inset: 0;
  }
  .let-tab-shape {
    position: absolute;
    left: 0;
    top: 0;
  }
  .let-tab {
    position: absolute;
    left: 63px;
    top: 0;
    width: 193px;
    height: 273px;
  }
  .let-tab span {
    position: absolute;
    left: 0;
    width: 100%;
    text-align: center;
    color: var(--paper);
    font-weight: 300;
    font-size: 84px;
    line-height: 1;
    letter-spacing: 2px;
  }
  .let-tab .to { top: 28px; }
  .let-tab .let { top: 128px; }
  .topiary {
    position: absolute;
    left: 366px;
    top: 109px;
    width: 97px;
    height: 196px;
    background: linear-gradient(180deg, rgba(255,255,255,0.85), rgba(255,255,255,0.6));
    border-radius: 48px 48px 6px 6px;
  }
  .rule {
    position: absolute;
    height: 1px;
    background: var(--line);
  }
  .rule.left { left: 150px; top: 291px; width: 207px; }
  .rule.right { left: 466px; top: 291px; width: 205px; }
  .rule.under { left: 150px; top: 578px; width: 515px; }
  .development-name {
    position: absolute;
    left: 0;
    top: 302px;
    width: 800px;
    margin: 0;
    text-align: center;
    color: var(--paper);
    font-family: "Cormorant Garamond", Georgia, serif;
    font-weight: 400;
    font-size: 142px;
    line-height: 132px;
  }
  .offer {
    position: absolute;
    left: 0;
    top: 628px;
    width: 800px;
    margin: 0;
    text-align: center;
    color: var(--paper);
    font-weight: 300;
    font-size: 50px;
    line-height: 63px;
    letter-spacing: 1px;
  }
  .agent-name {
    position: absolute;
    left: 276px;
    top: 913px;
    width: 265px;
    height: 121px;
    display: flex;
    align-items: center;
    justify-content: center;
    gap: 12px;
    background: var(--paper);
    box-shadow: 0 6px 14px rgba(0,0,0,0.25);
    color: var(--blue-deep);
    font-weight: 600;
    font-size: 30px;
  }
  .agent-name .mark {
    width: 16px;
    height: 16px;
    background: var(--blue-deep);
  }
  .contact {
    position: absolute;
    left: 0;
    top: 1066px;
    width: 800px;
    text-align: center;
    color: var(--ink);
    font-weight: 400;
    font-size: 25px;
  }
  .contact .gap { display: inline-block; width: 22px; }
  .base-band {
    position: absolute;
    left: 0;
    top: 1113px;
    width: 800px;
    height: 87px;
    background: linear-gradient(90deg, #7a7a7a 0%, var(--grey) 45%, #f4f4f4 85%, #9a9a9a 100%);
  }
</style>
</head>
<body>
<div class="poster">
  <div class="hero-panel">
    <svg class="swoosh" width="800" height="912" viewBox="0 0 800 912" aria-hidden="true">
      <path d="M0 640 C 250 520, 500 430, 800 400 L 800 912 L 0 912 Z" fill="#0f63dc" opacity="0.55"/>
      <path d="M120 912 C 300 720, 520 560, 740 450 C 560 600, 400 760, 300 912 Z" fill="#39c6ff" opacity="0.35"/>
      <path d="M230 912 C 380 780, 560 660, 700 560 C 580 680, 470 800, 400 912 Z" fill="#5ad6ff" opacity="0.3"/>
    </svg>
  </div>

  <svg class="let-tab-shape" width="800" height="300" aria-hidden="true">
    <defs>
      <linearGradient id="tabFill" x1="0" y1="0" x2="1" y2="1">
        <stop offset="0" stop-color="#2f8cf0"/>
        <stop offset="1" stop-color="#1a5fd6"/>
      </linearGradient>
    </defs>
    <path d="M63 0 H256 V238 L160 273 L63 238 Z" fill="url(#tabFill)"/>
    <path d="M48 46 L63 0 V46 Z" fill="#0a4fb0"/>
  </svg>
  <div class="let-tab">
    <span class="to">TO</span>
    <span class="let">LET</span>
  </div>

  <div class="topiary" role="img" aria-label="Line illustration of a clipped topiary tree in a planter"></div>
  <div class="rule left"></div>
  <div class="rule right"></div>

  <h1 class="development-name">Verrow<br>Gardens</h1>
  <div class="rule under"></div>

  <p class="offer">LUXURY<br>FULLY FURNISHED<br>LARGE 2 &amp; 3 BED<br>APARTMENTS</p>

  <div class="agent-name"><span class="mark"></span>Tallick Estates</div>

  <div class="contact">Telephone: 362 4105<span class="gap"></span>www.tallickestates-example.com</div>
  <div class="base-band"></div>
</div>
</body>
</html>
```